Web Design - 1 page for Buy - Repair - Service - Upgrade - PC Maintenance

We specialize in consumer and small business. It will be mobile friendly, viewable on all devices. Fully editable at the text level of the sections !!! - HTML / CSS only to be able to add a section would be to the web site
Updates

Target Market(s)

consumer and small business IT.

Coding

Coded - Design and coding required

Number of Pages Required

1 page

Font styles to use
Sans Serif

Requirements
Must have
• Looking for a page with a design that compliments the business card and pamphlet that has already been made (attached files). It should look professional and easy to read business. Email and phone number should be visible when the page loads. I do not want any forms for people to mess with. No "Contact Us" form or enter in email for newsletter. Customers will just be looking for this site to confirm we are professionals and have our business in order. OpenStreetMap: embedding map in webpage (like Google Maps) to where the workshop is located
Nice to have
• 2vask.com => this style of website would be more modern visually by integrating higher demands

```html
<!DOCTYPE html>
<html lang="en">
<head>
<meta charset="utf-8">
<title>Norvale Tech – PC / Vexa / Laptop Hardware Repair</title>
<link href="https://fonts.googleapis.com/css2?family=Montserrat:ital,wght@0,400;0,500;0,600;0,700;1,400&display=swap" rel="stylesheet">
<style>
:root{
  --blue:#2d8ad6;
  --blue-dark:#1f6fb5;
  --ink:#1b1b1b;
  --text:#333;
  --muted:#666;
  --grey-bg:#f3f3f3;
  --bar-bg:#eeeeee;
  --white:#fff;
  --star:#f2a900;
}
*{box-sizing:border-box;margin:0;padding:0}
html,body{width:1200px;height:3564px;overflow:hidden}
body{font-family:"Montserrat",sans-serif;color:var(--text);background:var(--white);position:relative}
.wrap{width:930px;margin:0 auto;position:relative}

/* header */
.site-header{height:100px;position:relative;background:var(--white)}
.brand{position:absolute;left:135px;top:30px;display:flex;align-items:center;gap:10px}
.brand-mark{width:26px;height:26px;background:var(--blue);border-radius:50%}
.brand-name{font-weight:700;font-size:20px;color:var(--blue-dark)}
.info-bar{position:absolute;left:495px;top:0;width:570px;height:36px;background:var(--bar-bg);display:flex;align-items:center;gap:26px;padding-left:22px;font-size:10.5px;color:#444}
.info-bar span{display:flex;align-items:center;gap:6px}
.info-bar svg{width:11px;height:11px;fill:var(--blue)}
.main-nav{position:absolute;left:495px;top:52px;width:570px;display:flex;align-items:center;font-size:12px;color:var(--ink);font-weight:500}
.main-nav a{color:inherit;text-decoration:none;margin-right:52px}
.main-nav .shop-btn{margin:0 0 0 auto;background:var(--blue);color:var(--white);font-size:10.5px;padding:11px 18px;border-radius:2px}

/* hero */
.hero{height:546px;position:relative;background:linear-gradient(90deg,#0d1a28 0%,#1e2f40 55%,#3a4753 100%);color:var(--white)}
.hero-title{position:absolute;left:138px;top:172px;font-size:46px;font-weight:600;line-height:54px}
.hero-title .accent{color:var(--blue);display:block}
.hero-text{position:absolute;left:138px;top:292px;width:620px;font-size:15px;line-height:22px;font-weight:500}
.btn{display:inline-block;background:var(--blue);color:var(--white);font-size:12px;font-weight:600;text-transform:uppercase;text-align:center;text-decoration:none;border-radius:2px}
.hero .btn{position:absolute;left:140px;top:358px;width:255px;height:40px;line-height:40px}

/* section headings */
.section-title{text-align:center;font-size:33px;font-weight:500;color:var(--ink)}
.section-lead{text-align:center;font-size:14px;line-height:21px;font-weight:500;margin:14px auto 0;width:640px}

/* problems */
.problems{height:1072px;padding-top:108px}
.service-grid{display:grid;grid-template-columns:repeat(3,320px);grid-auto-rows:240px;margin-top:58px}
.service{display:flex;gap:14px}
.service svg{flex:0 0 58px;width:58px;height:58px;stroke:var(--blue);fill:none;stroke-width:2.5}
.service h3{font-size:14px;font-weight:500;color:var(--blue);margin-bottom:4px}
.service p{font-size:12.5px;line-height:23px;color:#333;width:195px}

/* solutions */
.solutions{height:606px;background:var(--blue);color:var(--white);padding-top:84px;border-radius:4px 4px 0 0}
.solutions .section-title{color:var(--white)}
.photo-row{display:flex;justify-content:space-between;margin-top:48px}
.photo{width:449px;height:248px;background:linear-gradient(135deg,#c8b8a8,#8a7e74 60%,#5d6670)}
.photo.laptop{background:linear-gradient(135deg,#e9ecef,#b9c3cc 55%,#6f8192)}
.solutions .btn{display:block;margin:42px auto 0;width:255px;height:40px;line-height:40px;background:var(--white);color:#333;font-weight:500}

/* testimonials */
.testimonials{height:628px;background:var(--grey-bg);padding-top:98px}
.cards{display:flex;justify-content:space-between;margin-top:44px;padding:0 13px}
.card{background:var(--white);width:280px;height:272px;padding:40px 28px 0;box-shadow:0 2px 8px rgba(0,0,0,.06)}
.card h4{font-size:14px;font-weight:600;color:var(--ink);line-height:19px}
.card p{font-size:11px;line-height:17px;font-style:italic;color:#888;margin-top:10px}
.author{margin-top:14px;display:flex;align-items:center;gap:8px;font-size:12px;font-weight:500;color:var(--ink)}
.author::before{content:"";width:32px;height:1px;background:#bbb}
.author small{font-size:9px;color:#888;font-weight:400}
.stars{color:var(--star);font-size:12px;letter-spacing:1px;margin:6px 0 0 154px}

/* promo */
.promo{height:362px;background:linear-gradient(90deg,#0c1a2a 0%,#1a2f46 50%,#2e4c6d 100%);color:var(--white);position:relative}
.promo h2{position:absolute;left:138px;top:68px;font-size:34px;font-weight:500;line-height:42px}
.promo p{position:absolute;left:138px;top:175px;width:560px;font-size:15px;line-height:22px;font-weight:500}
.promo .btn{position:absolute;left:138px;top:268px;width:255px;height:40px;line-height:40px}

/* footer */
.site-footer{height:254px;background:var(--grey-bg);position:relative;font-size:12.5px;color:#333}
.footer-col{position:absolute;top:58px;line-height:20px}
.footer-col h5{font-size:14px;font-weight:500;color:var(--ink);margin-bottom:8px}
.contact{left:136px}
.shop{left:412px}
.map{position:absolute;left:706px;top:-54px;width:494px;height:308px;background:linear-gradient(135deg,#eadfd2,#e6cfc0 40%,#d9d4e8 100%);clip-path:polygon(16% 0,100% 0,100% 100%,0 100%,0 40%)}
.map-pin{position:absolute;left:232px;top:99px;width:30px;height:40px}
.copyright{position:absolute;left:136px;top:218px;font-size:10.5px;color:#333}
</style>
</head>
<body>

<header class="site-header">
  <div class="brand"><span class="brand-mark"></span><span class="brand-name">Norvale Tech</span></div>
  <div class="info-bar">
    <span><svg viewBox="0 0 10 10"><path d="M5 0a3.5 3.5 0 0 0-3.5 3.5C1.5 6 5 10 5 10s3.5-4 3.5-6.5A3.5 3.5 0 0 0 5 0zm0 5a1.5 1.5 0 1 1 0-3 1.5 1.5 0 0 1 0 3z"/></svg>48 Harbor Lane, Eastbrook, VIC 3100</span>
    <span><svg viewBox="0 0 10 10"><circle cx="5" cy="5" r="4.5" fill="none" stroke="#2d8ad6"/><path d="M5 2v3h2" fill="none" stroke="#2d8ad6"/></svg>Mon-Sat 8:00AM to 8:00PM</span>
    <span><svg viewBox="0 0 10 10"><path d="M2 0l2 2-1 1.5c.6 1.4 2 2.8 3.5 3.5L8 6l2 2-1.5 2C4 9.5.5 6 0 1.5z"/></svg>+1 555-010-2468</span>
  </div>
  <nav class="main-nav">
    <a href="#">Home</a><a href="#">Problems</a><a href="#">Solutions</a><a href="#">Testimonials</a>
    <a class="shop-btn" href="#">VISIT OUR SHOP</a>
  </nav>
</header>

<section class="hero" role="img" aria-label="Technician repairing a computer circuit board with a screwdriver">
  <h1 class="hero-title">PC / Vexa / Laptop<span class="accent">Hardware Repair Services</span></h1>
  <p class="hero-text">Lorem ipsum dolor sit amet, consectetur adipisicing elit, sed do eiusmod tempor incididunt ut labore et dolore magna aliqua.</p>
  <a class="btn" href="#">Visit our store today!</a>
</section>

<section class="problems">
  <div class="wrap">
    <h2 class="section-title">Have A Problem With Your Computer?</h2>
    <p class="section-lead">Lorem ipsum dolor sit amet, consectetur adipisicing elit, sed do eiusmod tempor incididunt ut labore et dolore magna aliqua.</p>
    <div class="service-grid">
      <div class="service">
        <svg viewBox="0 0 60 60"><path d="M20 34V12a3 3 0 0 1 6 0v16M26 26V8a3 3 0 0 1 6 0v18M32 26V10a3 3 0 0 1 6 0v18M38 28v-8a3 3 0 0 1 6 0v16c0 10-6 16-14 16s-12-4-16-12l-4-8a3 3 0 0 1 5-3l5 7"/><path d="M36 40c2-3 6-2 6 1s-6 6-6 6-6-3-6-6 4-4 6-1z"/></svg>
        <div><h3>Honest Service</h3><p>Our certified technicians aren't paid on commission. No pressure to upgrade to products/services you don't need or want. Even the best computers will eventually break down, and if we leave you happy, that's when we hope you'll come back to us.</p></div>
      </div>
      <div class="service">
        <svg viewBox="0 0 60 60"><rect x="4" y="10" width="52" height="34" rx="2"/><path d="M20 54h20M30 44v10"/><path d="M30 16l9 4v7c0 6-4 9-9 11-5-2-9-5-9-11v-7z"/><path d="M26 27l3 3 6-6"/></svg>
        <div><h3>Malware/Virus Removal</h3><p>Infections can come from many places and sometimes antivirus just isn't enough. We can get your system back to top shape, and train users how to avoid pitfalls in the future, which is better than any antivirus you could buy!</p></div>
      </div>
      <div class="service">
        <svg viewBox="0 0 60 60"><circle cx="30" cy="30" r="10"/><path d="M30 6v8M30 46v8M6 30h8M46 30h8M13 13l6 6M41 41l6 6M13 47l6-6M41 19l6-6"/><circle cx="30" cy="30" r="3"/></svg>
        <div><h3>PC/Vexa/Laptop Hardware Repair</h3><p>Find out exactly which part of your computer is failing and causing trouble. Our professionals will find the best value replacement and install it, good as new.</p></div>
      </div>
      <div class="service">
        <svg viewBox="0 0 60 60"><rect x="4" y="20" width="52" height="20"/><path d="M10 40v6M18 40v6M26 40v6M34 40v6M42 40v6M50 40v6"/><rect x="10" y="25" width="8" height="10"/><rect x="22" y="25" width="8" height="10"/><rect x="34" y="25" width="8" height="10"/></svg>
        <div><h3>Upgrades</h3><p>A new video card to play the latest game at the highest settings? A new disk to give your laptop a very noticable speed boost? Or maybe just the latest and greatest version of Panelo OS to keep you secure. We can make the upgrade hassle-free.</p></div>
      </div>
      <div class="service">
        <svg viewBox="0 0 60 60"><path d="M8 6h24l8 8v36H8z"/><path d="M14 20h18M14 28h18M14 36h12"/><circle cx="44" cy="42" r="10"/><path d="M40 42h8M45 38l3 4-3 4"/></svg>
        <div><h3>Data Migration</h3><p>We can make your new computer feel like an old friend. Transfer all your files, photos, bookmarks, email accounts, personal settings, etc. to a new computer and put them right where you left them.</p></div>
      </div>
      <div class="service">
        <svg viewBox="0 0 60 60"><circle cx="25" cy="25" r="17"/><path d="M37 37l15 15"/><path d="M18 25a7 7 0 0 1 7-7"/></svg>
        <div><h3>Data Rescue</h3><p>Flash drive formatted? Hard Drive corrupted? Data loss can be devastating, but sometimes recovery is possible for precious photos and important documents. If our best tools can't get your files back, you won't be charged.</p></div>
      </div>
      <div class="service">
        <svg viewBox="0 0 60 60"><path d="M8 40a22 22 0 1 1 44 0"/><path d="M30 40l10-14"/><circle cx="30" cy="40" r="3"/><path d="M14 40h4M42 40h4M30 20v4"/></svg>
        <div><h3>Tune Ups</h3><p>Over time, systems can get slowed down by unnecessary files and programs demanding attention from your processor and memory that should instead be doing work for you! We can clean up (and physically clean out) your system to get it running at peak performance.</p></div>
      </div>
      <div class="service">
        <svg viewBox="0 0 60 60"><rect x="6" y="18" width="48" height="32" rx="3"/><path d="M22 18v-6h16v6M6 30h48M26 30v6h8v-6"/></svg>
        <div><h3>In-Home Installation</h3><p>All our services come with pick-up and drop-off installation. You won't be left to set up wireless networking, cables, controllers, and printers by yourself.</p></div>
      </div>
      <div class="service">
        <svg viewBox="0 0 60 60"><circle cx="30" cy="30" r="24"/><ellipse cx="30" cy="30" rx="10" ry="24"/><path d="M6 30h48M10 18h40M10 42h40"/></svg>
        <div><h3>Remote Support</h3><p>Small problems shouldn't cost an arm and a leg to fix. We'll set up remote support to your computer to efficiently and cost effectively solve what can be solved without the need of a sending a technician over.</p></div>
      </div>
    </div>
  </div>
</section>

<section class="solutions">
  <div class="wrap">
    <h2 class="section-title">Flexible Solutions To Your Problems</h2>
    <p class="section-lead">Lorem ipsum dolor sit amet, consectetur adipisicing elit, sed do eiusmod tempor incididunt ut labore et dolore magna aliqua.</p>
    <div class="photo-row">
      <div class="photo repair" role="img" aria-label="Two technicians testing the inside of an open desktop computer"></div>
      <div class="photo laptop" role="img" aria-label="Hands typing on a laptop showing an error message on screen"></div>
    </div>
    <a class="btn" href="#">Visit our store today!</a>
  </div>
</section>

<section class="testimonials">
  <div class="wrap">
    <h2 class="section-title">Read what our customers say?</h2>
    <p class="section-lead">Lorem ipsum dolor sit amet, consectetur adipisicing elit, sed do eiusmod tempor incididunt ut labore et dolore magna aliqua.</p>
    <div class="cards">
      <article class="card">
        <h4>Smart, Fast &amp; Reliable</h4>
        <p>Lorem ipsum dolor sit amet, consectetur adipisicing elit, sed do eiusmod tempor incididunt ut labore et dolore magna aliqua. Ut enim ad minim veniam, quis nostrud exercitation ullamco.</p>
        <div class="author">Jon Carter <small>- Coney Island</small></div>
        <div class="stars">★★★★</div>
      </article>
      <article class="card">
        <h4>Professional, Reliable, Friendly and Quality Service</h4>
        <p>Quis nostrud exercitation ullamco laboris nisi ut aliquip ex ea commodo consequat. Duis aute irure dolor in reprehenderit in voluptate velit esse cillum dolore eu.</p>
        <div class="author">Drew Doe <small>- Sacramento, CA</small></div>
        <div class="stars">★★★★★</div>
      </article>
      <article class="card">
        <h4>Incredible Service!</h4>
        <p>Mollit anim id est laborum. Sed ut perspiciatis unde omnis iste natus error sit voluptatem accusantium doloremque laudantium, totam rem aperiam, eaque ipsa quae ab illo inventore veritatis et.</p>
        <div class="author">Sam Rivers <small>- Charleston, SC</small></div>
        <div class="stars">★★★★</div>
      </article>
    </div>
  </div>
</section>

<section class="promo" role="img" aria-label="Close-up of a computer motherboard in blue light">
  <h2>Save 20% on PC / Vexa /<br>Laptop Hardware Repair</h2>
  <p>Find out exactly which part of your computer is failing and causing trouble. Our professionals will find the best value replacement and install it, good as new.</p>
  <a class="btn" href="#">Visit our store today!</a>
</section>

<footer class="site-footer">
  <div class="footer-col contact">
    <h5>Contact us</h5>
    Call us: +1 555-010-2468<br>E-mail: mail@norvaletech.com
  </div>
  <div class="footer-col shop">
    <h5>Visit our Shop</h5>
    48 Harbor Lane, Eastbrook,<br>Victoria 3100 Australia
  </div>
  <div class="map" role="img" aria-label="Street map showing the workshop location">
    <svg class="map-pin" viewBox="0 0 30 40"><path d="M15 0A15 15 0 0 0 0 15c0 11 15 25 15 25s15-14 15-25A15 15 0 0 0 15 0z" fill="#2d8ad6"/><circle cx="15" cy="15" r="6" fill="#fff"/></svg>
  </div>
  <p class="copyright">© 2019 NORVALE TECH . All Rights Reserved</p>
</footer>

</body>
</html>
```